Waterproofing Adhesive company needs design for bucket

We need a design for our 20kg/15kg and 4 kg bucket, Our companys name is Zorvane Co LLC based in Umm Al Quwain, United Arab Emirates . Our main business is into waterproofing paint and Adhesive manufacturing. We are looking for a creative design for our buckets and paper bags. The design have to be attractive, The color theme of our company is light orange and yellow. I have attached the company logo along with this.

Target Market(s)

B2b , construction companys
Maintenance company

Industry/Entity Type

Manufacturer

Requirements
Must have
• It must have the company logo
• a spcae in centre to write the different products names
Nice to have
• A attractive design for placing the bucket in retail shops

```html
<!DOCTYPE html>
<html lang="en">
<head>
<meta charset="utf-8">
<title>Zorvane Co LLC – Waterproofing Bucket Label</title>
<link href="https://fonts.googleapis.com/css2?family=Alfa+Slab+One&family=Montserrat:ital,wght@0,700;1,800;1,900&family=Roboto+Condensed:wght@400;700&display=swap" rel="stylesheet">
<style>
  :root {
    --canvas: #ececec;
    --paper: #ffffff;
    --amber: #f2b705;
    --amber-deep: #f0a000;
    --lemon: #f6ef00;
    --orange: #ef8a1c;
    --rust: #c9471c;
    --ink: #0d0d0d;
    --grey: #8a8a8a;
  }
  * { margin: 0; padding: 0; box-sizing: border-box; }
  html, body { width: 1200px; height: 1200px; overflow: hidden; background: var(--canvas); }
  .label {
    position: absolute; left: 60px; top: 150px;
    width: 1080px; height: 900px;
    background: var(--paper);
    overflow: hidden;
    font-family: "Montserrat", sans-serif;
  }
  .label svg.art { position: absolute; left: 0; top: 0; }
  .divider { position: absolute; top: 0; width: 5px; height: 175px; background: var(--amber-deep); }
  .brand {
    position: absolute; left: 380px; width: 322px; top: 88px;
    display: flex; align-items: center; justify-content: center; gap: 10px;
  }
  .brand-mark { width: 26px; height: 26px; background: var(--orange); }
  .brand-name { font-family: "Montserrat", sans-serif; font-weight: 700; font-size: 24px; color: var(--orange); }
  .product-title {
    position: absolute; left: 205px; top: 228px;
    font-family: "Alfa Slab One", serif; font-size: 104px; letter-spacing: 4px;
    color: var(--amber); line-height: 1;
  }
  .product-subtitle {
    position: absolute; left: 563px; top: 337px; width: 276px; height: 48px;
    background: var(--rust); transform: skewX(-12deg);
    display: flex; align-items: center; justify-content: center;
  }
  .product-subtitle span {
    transform: skewX(12deg); font-style: italic; font-weight: 900; font-size: 42px;
    color: var(--paper); letter-spacing: 3px;
  }
  .headline {
    position: absolute; font-style: italic; font-weight: 900; font-size: 44px;
    color: var(--ink); line-height: 1; letter-spacing: 2px;
  }
  .headline.first { left: 224px; top: 436px; }
  .headline.second { left: 388px; top: 488px; }
  .pointer { position: absolute; left: 356px; top: 496px; }
  .category {
    position: absolute; left: 178px; top: 543px; width: 672px; height: 64px;
    background: var(--paper); transform: skewX(-14deg);
    border-bottom: 8px solid var(--rust);
    display: flex; align-items: center; justify-content: center;
  }
  .category span {
    transform: skewX(14deg); font-style: italic; font-weight: 900; font-size: 54px;
    color: var(--orange); letter-spacing: 3px;
  }
  .features {
    position: absolute; left: 184px; top: 640px; width: 760px;
    display: grid; grid-template-columns: 362px 362px; row-gap: 14px;
    list-style: none;
  }
  .features li {
    display: flex; align-items: center; gap: 14px;
    font-family: "Roboto Condensed", sans-serif; font-size: 17px; color: #2a2a2a; height: 23px;
  }
  .net {
    position: absolute; left: 190px; top: 804px;
  }
  .net-label { font-family: "Roboto Condensed", sans-serif; font-weight: 700; font-size: 16px; color: var(--ink); }
  .net-value { font-family: "Alfa Slab One", serif; font-size: 46px; color: var(--orange); line-height: 1; margin-top: -2px; }
  .base-line { position: absolute; left: 50px; top: 868px; width: 1030px; height: 16px; background: var(--lemon); }
</style>
</head>
<body>
  <section class="label">
    <svg class="art" width="1080" height="900" viewBox="0 0 1080 900">
      <defs>
        <linearGradient id="topBand" x1="0" y1="0" x2="0" y2="1">
          <stop offset="0" stop-color="#f7c20a"/>
          <stop offset="1" stop-color="#f0a400"/>
        </linearGradient>
        <linearGradient id="lowerBand" x1="0" y1="0" x2="0" y2="1">
          <stop offset="0" stop-color="#f1b800"/>
          <stop offset="0.35" stop-color="#f6dc00"/>
          <stop offset="1" stop-color="#f7f200"/>
        </linearGradient>
      </defs>
      <path role="img" aria-label="Yellow paint splash band, left" fill="url(#topBand)"
        d="M0 0 H372 V175 C340 170 320 150 290 160 C250 140 220 110 180 120 C140 100 110 125 70 108 C40 102 20 120 0 118 Z"/>
      <path role="img" aria-label="Yellow paint splash band, right" fill="url(#topBand)"
        d="M708 0 H1080 V95 C1040 110 1010 92 970 110 C930 98 900 120 860 112 C820 118 790 105 760 130 C735 125 720 140 708 140 Z"/>
      <path role="img" aria-label="Yellow paint splash background" fill="url(#lowerBand)"
        d="M0 460 C40 440 80 470 130 452 C180 430 220 462 260 440 C320 445 380 420 440 430 C520 400 600 380 660 392 C720 380 780 420 840 440 C900 448 960 420 1010 450 C1040 455 1060 440 1080 448 V790 H0 Z"/>
    </svg>

    <div class="divider" style="left:378px"></div>
    <div class="divider" style="left:700px"></div>

    <div class="brand">
      <span class="brand-mark"></span>
      <span class="brand-name">Zorvane Co LLC</span>
    </div>

    <h1 class="product-title">PRODUCT</h1>
    <div class="product-subtitle"><span>NAME</span></div>

    <p class="headline first">LOREM IPSUM</p>
    <svg class="pointer" width="26" height="30" viewBox="0 0 26 30"><polygon points="26,0 26,30 0,15" fill="var(--rust)"/></svg>
    <p class="headline second">DUMMY TEXT.</p>

    <div class="category"><span>WATERPROOFING</span></div>

    <ul class="features">
      <li><svg width="20" height="18" viewBox="0 0 20 18"><path d="M2 9 L8 15 L18 2" fill="none" stroke="var(--rust)" stroke-width="3"/></svg>Lorem Ipsum is simply dummy text.</li>
      <li><svg width="20" height="18" viewBox="0 0 20 18"><path d="M2 9 L8 15 L18 2" fill="none" stroke="var(--rust)" stroke-width="3"/></svg>Lorem Ipsum is simply dummy text.</li>
      <li><svg width="20" height="18" viewBox="0 0 20 18"><path d="M2 9 L8 15 L18 2" fill="none" stroke="var(--rust)" stroke-width="3"/></svg>Lorem Ipsum is simply dummy text.</li>
      <li><svg width="20" height="18" viewBox="0 0 20 18"><path d="M2 9 L8 15 L18 2" fill="none" stroke="var(--rust)" stroke-width="3"/></svg>Lorem Ipsum is simply dummy text.</li>
      <li><svg width="20" height="18" viewBox="0 0 20 18"><path d="M2 9 L8 15 L18 2" fill="none" stroke="var(--rust)" stroke-width="3"/></svg>Lorem Ipsum is simply dummy text.</li>
      <li><svg width="20" height="18" viewBox="0 0 20 18"><path d="M2 9 L8 15 L18 2" fill="none" stroke="var(--rust)" stroke-width="3"/></svg>Lorem Ipsum is simply dummy text.</li>
      <li><svg width="20" height="18" viewBox="0 0 20 18"><path d="M2 9 L8 15 L18 2" fill="none" stroke="var(--rust)" stroke-width="3"/></svg>Lorem Ipsum is simply dummy text.</li>
      <li><svg width="20" height="18" viewBox="0 0 20 18"><path d="M2 9 L8 15 L18 2" fill="none" stroke="var(--rust)" stroke-width="3"/></svg>Lorem Ipsum is simply dummy text.</li>
    </ul>

    <div class="net">
      <p class="net-label">Net Wt.</p>
      <p class="net-value">20kg</p>
    </div>
    <div class="base-line"></div>
  </section>
</body>
</html>
```